Digital Menu Board for Restaurant

I want a digital menu board for our new restaurant. I have provided the sample of what I kind of want.
This is to be on a 55 inch tv so it needs to be the correct aspect ratio of 4:5

Font styles to use
Serif
Sans Serif

Colors
f59296
f04a50
ec1f27
ffffff
fffef7
fbed22
ffc214
0592cd
e5519f

Requirements
Must have
• fun, maybe something moving? bright colors on a darker background so it's easy to read or dark font on a light background.

```html
<!DOCTYPE html>
<html lang="en">
<head>
<meta charset="utf-8">
<title>Sandy Cove Menu Board</title>
<link href="https://fonts.googleapis.com/css2?family=Oswald:wght@700&family=Rubik:ital,wght@0,800;1,800;1,900&display=swap" rel="stylesheet">
<style>
  :root{
    --red:#ec1f27;
    --coral:#f04a50;
    --white:#ffffff;
    --cream:#fffef7;
    --yellow:#fbed22;
    --gold:#ffc214;
    --blue:#0592cd;
    --title-blue:#1a80c8;
    --pink:#e5519f;
    --plum:#b93f8c;
    --desc:#c8245a;
    --kids:#c4307e;
    --green:#7cbf3a;
  }
  *{margin:0;padding:0;box-sizing:border-box}
  html,body{width:897px;height:1200px;overflow:hidden;background:#f1f1f1}
  .board{position:absolute;left:18px;top:356px;width:860px;height:487px;background:var(--white);overflow:hidden;font-family:'Rubik',sans-serif}
  .block{position:absolute}
  .band-title{font-family:'Oswald',sans-serif;font-weight:700;color:var(--white);text-transform:uppercase;line-height:1;letter-spacing:.5px}

  /* left column */
  .buns-head{left:0;top:0;width:316px;height:67px;background:var(--red)}
  .buns-head .band-title{position:absolute;left:20px;top:14px;font-size:38px}
  .buns-list{left:0;top:67px;width:316px;height:316px;padding:4px 0 0 24px;background:var(--cream)}
  .item{margin-bottom:5px}
  .item-name{font-style:italic;font-weight:900;color:var(--title-blue);font-size:19px;line-height:1.05}
  .item-desc{font-style:italic;font-weight:800;color:var(--desc);font-size:10.3px;line-height:13px}
  .combo-head{left:0;top:383px;width:316px;height:38px;background:var(--blue)}
  .combo-head .band-title{position:absolute;left:24px;top:3px;font-size:32px}
  .combo-list{left:0;top:421px;width:316px;height:66px;background:var(--pink);padding:4px 0 0 24px}
  .combo-list li{list-style:none;font-style:italic;font-weight:900;color:var(--white);font-size:15.5px;line-height:18.5px}

  /* center column */
  .brand-photo{left:316px;top:60px;width:225px;height:165px;background:linear-gradient(160deg,#3f8fc0 0%,#c59a66 45%,#6b4630 75%,#3c3b3a 100%)}
  .brand-panel{left:316px;top:0;width:225px;height:160px}
  .brand-name{left:316px;top:40px;width:225px;text-align:center;font-weight:800;font-size:30px;color:var(--coral);line-height:1}
  .kids-head{left:316px;top:225px;width:225px;height:33px;background:var(--red)}
  .kids-head .band-title{position:absolute;left:5px;top:6px;font-size:21px;white-space:nowrap}
  .kids-head small{font-size:13px}
  .kids-list,.shake-list{left:316px;width:225px;padding-left:11px;background:var(--cream)}
  .kids-list{top:258px;height:73px;padding-top:6px}
  .small-list li{list-style:none;font-style:italic;font-weight:800;color:var(--kids);font-size:10px;line-height:12.4px}
  .shakes-head{left:316px;top:331px;width:225px;height:32px;background:var(--blue);text-align:center}
  .shakes-head .band-title{font-size:28px;padding-top:1px}
  .shake-list{top:363px;height:124px;padding-top:5px}
  .shake-list li{line-height:12.9px}

  /* right column */
  .shore-head{left:541px;top:0;width:319px;height:67px;background:var(--red)}
  .shore-head .band-title{position:absolute;left:18px;top:14px;font-size:38px}
  .shore-list{left:541px;top:67px;width:319px;height:231px;padding:4px 0 0 21px;background:var(--cream)}
  .shore-list .item{margin-bottom:4px}
  .side-head{left:541px;top:298px;width:149px;height:33px;background:var(--blue)}
  .drinks-head{left:691px;top:298px;width:169px;height:33px;background:var(--blue)}
  .side-head .band-title,.drinks-head .band-title{position:absolute;left:22px;top:2px;font-size:28px}
  .drinks-head .band-title{left:9px}
  .side-list{left:541px;top:331px;width:149px;height:156px;background:var(--plum);padding:9px 0 0 21px}
  .side-list li{list-style:none;font-style:italic;font-weight:900;color:var(--white);font-size:11.5px;line-height:16.8px}
  .drinks-list{left:691px;top:331px;width:169px;height:156px;background:var(--yellow);display:grid;grid-template-columns:78px 70px;column-gap:6px;padding:9px 0 0 12px;align-content:start}
  .drinks-list li{list-style:none;font-style:italic;font-weight:900;color:var(--title-blue);font-size:11.5px;line-height:14.6px;white-space:nowrap}

  .shoreline{left:0;top:455px;width:860px;height:32px}
</style>
</head>
<body>
<main class="board">
  <section class="block buns-head"><h2 class="band-title">Between Buns</h2></section>
  <section class="block buns-list">
    <div class="item"><h3 class="item-name">1st Point Pulled Pork</h3><p class="item-desc">Pulled Pork, Marty's Sassy BBQ Sauce,<br>Chopped Bacon, Pepperjack Cheese, and Fried<br>Jalapeno Pepers on Ciabatta Bun</p></div>
    <div class="item"><h3 class="item-name">2nd Point Pulled Pork</h3><p class="item-desc">Pulled Pork, Marty's Sweet Raspberry BBQ<br>Sauce, and Coleslaw on a Ciabatta Bun</p></div>
    <div class="item"><h3 class="item-name">Spiniker Point Burger</h3><p class="item-desc">Smokehouse 1/2 Pound Burger, Crumbled<br>Bacon, Marty's Sassy BBQ Sauce, Cheese, and<br>Onion Rings on a Toasted Brioche Bun</p></div>
    <div class="item"><h3 class="item-name">The Rock Burger</h3><p class="item-desc">Two Smokehouse 1/2 Pound Patties, Cheese,<br>Lettuce, Tomato, Onion, Pickles, on toasted<br>Brioche Bun</p></div>
    <div class="item"><h3 class="item-name">Rainbow Cove Sandwich</h3><p class="item-desc">Chicken Salad - Smoked Chicken Celery, and<br>Onion Mixed with our BBQ Mayo and Topped<br>with Sea-soned Tomato on a Hoagie Roll.</p></div>
  </section>
  <section class="block combo-head"><h2 class="band-title">Combo Up!</h2></section>
  <ul class="block combo-list">
    <li>Add 1 Side and Drink</li>
    <li>Add 1 Side and Shake</li>
    <li>Additional Sides</li>
  </ul>

  <div class="block brand-photo" role="img" aria-label="Photo of a pulled pork sandwich with BBQ drizzle and sprouts on a wooden board"></div>
  <svg class="block brand-panel" viewBox="0 0 225 160" aria-hidden="true"><polygon points="0,0 225,0 225,107 112.5,156 0,107" fill="var(--yellow)"/></svg>
  <p class="block brand-name">Sandy Cove</p>
  <section class="block kids-head"><h2 class="band-title">Seashell Finders <small>(Kids)</small></h2></section>
  <ul class="block kids-list small-list">
    <li>Little Cheeseburger</li>
    <li>Pulled pork sandwich</li>
    <li>Mini Corn Dogs</li>
    <li>Chicken salad sandwich</li>
    <li>Fries/Onion Rings</li>
  </ul>
  <section class="block shakes-head"><h2 class="band-title">Shakes</h2></section>
  <ul class="block shake-list small-list">
    <li>Marty's Signature Raspberry<br>Jammin Shake</li>
    <li>Raspberry Cookie Crumble Shake</li>
    <li>Raspberry Hazelnut BombShake</li>
    <li>Raspberry Brownie Shake</li>
    <li>Caramel Shake</li>
    <li>Chocolate Shake</li>
    <li>Raspberry Beachin' Shake (Pina Colada)</li>
  </ul>

  <section class="block shore-head"><h2 class="band-title">Green Shore</h2></section>
  <section class="block shore-list">
    <div class="item"><h3 class="item-name">North Beach Salad</h3><p class="item-desc">Pulled pork and Black Beans on a Bed of<br>Romaine, tomato and Onion with Sweet and<br>Sour Raspberry Pineapple Sauce. West Side<br>Salad</p></div>
    <div class="item"><h3 class="item-name">West Side Salad</h3><p class="item-desc">BBQ Pulled Pork, Crumbled Bacon, Candied<br>Walnuts, Feta Cheese, Red Onion, Spinach and<br>Lettuce with Ranch Dressing or Raspberry<br>Vinaigrette</p></div>
    <div class="item"><h3 class="item-name">East Side Salad</h3><p class="item-desc">Spinach and Lettuce, Chopped Apples,<br>Candied Walnuts, Onion, Feta Cheese with<br>Marty's Raspberry Vinaigrette Add Chicken:</p></div>
  </section>
  <section class="block side-head"><h2 class="band-title">Side</h2></section>
  <section class="block drinks-head"><h2 class="band-title">Drinks</h2></section>
  <ul class="block side-list">
    <li>Seasoned Fries</li>
    <li>Onion Rings</li>
    <li>Sweet Cornbread</li>
    <li>Sweet Coleslaw</li>
    <li>Macaroni Salad</li>
    <li>Side Salad</li>
  </ul>
  <div class="block drinks-list">
    <ul><li>Zesto</li><li>Diet Zesto</li><li>Koola</li><li>Diet Koola</li><li>Hill Fizz</li></ul>
    <ul><li>Diet Fizz</li><li>Lemonade</li><li>Lime Up</li><li>Dr Spice</li></ul>
  </div>

  <svg class="block shoreline" viewBox="0 0 860 32" aria-hidden="true">
    <path d="M170 32 Q430 6 690 32 Z" fill="var(--green)"/>
    <path d="M200 32 Q430 14 660 32 Z" fill="var(--blue)"/>
  </svg>
</main>
</body>
</html>
```